Quellora business card design

create modern and tech looking business card that is clean but effectively communciates that we are a cloud communications company.
Should have at minimum:
Employee Name
Postion
Phone Number
Email
website
Contact Information for Business Card
create modern and tech looking business card that is clean but effectively communciates that we are a cloud communications company. We have two logo color schemes (attached) so would like to see designs both ways
Should have at minimum:
Employee Name
Postion
Phone Number
Email
website

```html
<!DOCTYPE html>
<html lang="en">
<head>
<meta charset="utf-8">
<title>Quellora business card</title>
<link rel="stylesheet" href="https://fonts.googleapis.com/css2?family=Open+Sans:wght@400;600&family=Arimo:wght@400&display=swap">
<style>
  :root {
    --purple: #65318f;
    --purple-soft: #7a4aa3;
    --cyan: #2fc0df;
    --ink: #555a60;
    --brand-ink: #45484d;
    --paper: #ffffff;
    --stage: #e9e9ec;
  }
  html, body {
    margin: 0;
    width: 1200px;
    height: 930px;
    overflow: hidden;
    background: var(--stage);
  }
  .canvas {
    position: relative;
    width: 1200px;
    height: 930px;
  }
  .card {
    position: absolute;
    width: 560px;
    height: 320px;
    border-radius: 16px;
    overflow: hidden;
    box-shadow: 0 6px 18px rgba(0,0,0,.15);
    font-family: "Open Sans", sans-serif;
  }
  .card--back {
    left: 60px;
    top: 110px;
    background: var(--purple);
  }
  .card--front {
    left: 580px;
    top: 490px;
    background: var(--paper);
  }
  .map-area {
    position: absolute;
    left: 70px;
    top: 40px;
    width: 420px;
    height: 210px;
    border-radius: 40px;
    background: radial-gradient(ellipse at center, var(--purple-soft) 0%, rgba(122,74,163,0) 70%);
  }
  .brand {
    position: absolute;
    display: flex;
    align-items: center;
    gap: 12px;
    font-weight: 600;
    letter-spacing: 2px;
    white-space: nowrap;
  }
  .brand__mark {
    width: 22px;
    height: 22px;
  }
  .card--back .brand {
    left: 50%;
    top: 128px;
    transform: translateX(-50%);
    color: var(--paper);
    font-size: 46px;
  }
  .card--back .brand__mark { background: var(--paper); }
  .back-url {
    position: absolute;
    bottom: 48px;
    width: 100%;
    text-align: center;
    color: var(--paper);
    font-size: 12px;
    letter-spacing: 1.5px;
  }
  .card--front .brand {
    left: 40px;
    top: 58px;
    color: var(--brand-ink);
    font-size: 38px;
  }
  .card--front .brand__mark { background: var(--cyan); }
  .person {
    position: absolute;
    right: 40px;
    top: 66px;
    text-align: right;
    font-family: "Arimo", sans-serif;
  }
  .person__name {
    color: var(--purple);
    font-size: 20px;
    letter-spacing: .5px;
  }
  .person__role {
    color: var(--cyan);
    font-size: 16px;
  }
  .address {
    position: absolute;
    left: 60px;
    top: 162px;
    color: var(--ink);
    font-size: 13px;
    line-height: 1.45;
    letter-spacing: .5px;
  }
  .contacts {
    position: absolute;
    left: 60px;
    top: 206px;
    margin: 0;
    padding: 0;
    list-style: none;
    color: var(--ink);
    font-size: 13px;
    line-height: 1.5;
    letter-spacing: .5px;
    z-index: 1;
  }
  .contacts li { display: flex; align-items: center; gap: 8px; }
  .contacts svg { width: 12px; height: 12px; flex: none; }
  .wave {
    position: absolute;
    left: 0;
    top: 0;
    width: 560px;
    height: 320px;
  }
</style>
</head>
<body>
<main class="canvas">
  <section class="card card--back">
    <div class="map-area" role="img" aria-label="Faint dotted world map"></div>
    <div class="brand"><span class="brand__mark"></span>Quellora</div>
    <div class="back-url">www.quellora.com</div>
  </section>

  <section class="card card--front">
    <svg class="wave" viewBox="0 0 560 320" aria-hidden="true">
      <path d="M0 292 C150 288 250 272 330 232 C420 188 490 160 560 146 L560 320 L0 320 Z" fill="var(--purple)"/>
      <path d="M0 296 C150 292 255 276 335 238 C425 194 495 166 560 150 L560 320 L0 320 Z" fill="var(--paper)"/>
      <path d="M0 299 C150 295 258 279 338 241 C428 197 498 168 560 153 L560 320 L0 320 Z" fill="var(--cyan)"/>
      <path d="M0 305 C150 301 262 287 345 250 C435 207 505 178 560 166 L560 320 L0 320 Z" fill="var(--purple)"/>
      <path d="M0 320 L0 310 C120 308 220 302 300 294 C380 286 470 300 560 320 Z" fill="var(--cyan)"/>
    </svg>
    <div class="brand"><span class="brand__mark"></span>Quellora</div>
    <div class="person">
      <div class="person__name">DANIEL REYES</div>
      <div class="person__role">Founder</div>
    </div>
    <div class="address">4820 Harbor Lane,<br>Suite Tempe 85281</div>
    <ul class="contacts">
      <li>
        <svg viewBox="0 0 12 12"><rect x="3" y="0.5" width="6" height="11" rx="1" fill="none" stroke="var(--cyan)" stroke-width="1.2"/></svg>
        0478 602 915
      </li>
      <li>
        <svg viewBox="0 0 12 12"><rect x="0.5" y="2" width="11" height="8" fill="var(--purple)"/><path d="M0.5 2 L6 7 L11.5 2" fill="none" stroke="#fff" stroke-width="1"/></svg>
        info@danielreyes.com
      </li>
      <li>
        <svg viewBox="0 0 12 12"><circle cx="5" cy="5" r="3.5" fill="none" stroke="var(--cyan)" stroke-width="1.6"/><line x1="7.5" y1="7.5" x2="11" y2="11" stroke="var(--cyan)" stroke-width="1.8"/></svg>
        www.quellora.com
      </li>
    </ul>
  </section>
</main>
</body>
</html>
```